Corwin Crest Homes Needs Business Card Design

Looking for a unique modern business card to fit my new Logo.
Name: Marcus Corwin
Company: Corwin Crest Homes, LLC
Tag Line: Always Built Better
Email: corwincresthomes@mailnest.example
Phone: (555) 017-2846
Website: www.corwincresthomes.example
License: CORWICH462KX

```html
<!DOCTYPE html>
<html lang="en">
<head>
<meta charset="UTF-8">
<title>Corwin Crest Homes — Business Card</title>
<link href="https://fonts.googleapis.com/css2?family=Montserrat:wght@400;500;700;800&display=swap" rel="stylesheet">
<style>
  :root {
    --page: #eeeff0;
    --ink: #111111;
    --card-dark: #121517;
    --card-light: #ffffff;
    --accent: #3fb1e6;
    --muted-logo: #8c9094;
    --tagline: #d6d8da;
    --divider: #3a3a3a;
  }
  * { margin: 0; padding: 0; box-sizing: border-box; }
  html, body {
    width: 1200px;
    height: 1005px;
    overflow: hidden;
    background: var(--page);
    font-family: "Montserrat", Arial, sans-serif;
  }
  .canvas {
    position: relative;
    width: 1200px;
    height: 1005px;
  }
  .card {
    position: absolute;
    left: 250px;
    width: 700px;
    height: 400px;
    box-shadow: 0 10px 30px rgba(0,0,0,0.12);
  }
  /* Back side */
  .card--back {
    top: 70px;
    background: var(--card-dark);
    border: 3px solid var(--accent);
    display: flex;
    flex-direction: column;
    align-items: center;
    justify-content: center;
  }
  .brand {
    display: flex;
    align-items: center;
    gap: 12px;
  }
  .brand__mark {
    width: 18px;
    height: 18px;
  }
  .brand__name {
    font-weight: 700;
    text-transform: uppercase;
    letter-spacing: 1px;
  }
  .card--back .brand__mark { background: var(--muted-logo); }
  .card--back .brand__name { color: var(--muted-logo); font-size: 30px; }
  .tagline {
    margin-top: 70px;
    color: var(--tagline);
    font-size: 17px;
    font-weight: 400;
    letter-spacing: 1.5px;
    text-transform: uppercase;
  }
  /* Front side */
  .card--front {
    top: 530px;
    background: var(--card-light);
    display: flex;
    align-items: center;
  }
  .card--front .brand {
    width: 330px;
    justify-content: center;
  }
  .card--front .brand__mark { background: var(--accent); }
  .card--front .brand__name {
    color: var(--ink);
    font-size: 21px;
    font-weight: 800;
    line-height: 1.15;
  }
  .divider {
    width: 2px;
    height: 200px;
    background: var(--divider);
  }
  .details {
    padding-left: 34px;
    color: var(--ink);
  }
  .details__name {
    color: var(--accent);
    font-size: 29px;
    font-weight: 800;
    letter-spacing: 0.5px;
    text-transform: uppercase;
  }
  .details__role {
    font-size: 17px;
    font-weight: 400;
    margin-top: 2px;
  }
  .details__company {
    font-size: 17px;
    font-weight: 700;
    margin-top: 10px;
  }
  .contact {
    list-style: none;
    margin-top: 14px;
    font-size: 16px;
  }
  .contact li {
    display: flex;
    align-items: center;
    gap: 8px;
    line-height: 1.55;
  }
  .contact svg { width: 14px; height: 14px; flex: none; }
  .details__license {
    margin-top: 4px;
    font-size: 16px;
    font-weight: 700;
  }
</style>
</head>
<body>
<main class="canvas">
  <section class="card card--back" aria-label="Card back">
    <div class="brand">
      <span class="brand__mark"></span>
      <span class="brand__name">Corwin Crest Homes</span>
    </div>
    <p class="tagline">Always Built Better</p>
  </section>

  <section class="card card--front" aria-label="Card front">
    <div class="brand">
      <span class="brand__mark"></span>
      <span class="brand__name">Corwin Crest<br>Homes</span>
    </div>
    <div class="divider"></div>
    <div class="details">
      <h1 class="details__name">Marcus Corwin</h1>
      <p class="details__role">Managing Director</p>
      <p class="details__company">Corwin Crest Homes, LLC</p>
      <ul class="contact">
        <li>
          <svg viewBox="0 0 16 16" aria-hidden="true"><path fill="var(--accent)" d="M3.5 1.5l2.5 0 1 3.5-1.6 1.2a8 8 0 0 0 4.4 4.4L11 9l3.5 1v2.5c0 1-1 2-2 2C6.5 14.5 1.5 9.5 1.5 3.5c0-1 1-2 2-2z"/></svg>
          (555) 017-2846
        </li>
        <li>
          <svg viewBox="0 0 16 16" aria-hidden="true"><rect x="1" y="3" width="14" height="10" rx="1" fill="var(--accent)"/><path d="M1.5 4l6.5 5 6.5-5" stroke="#fff" stroke-width="1.3" fill="none"/></svg>
          corwincresthomes@mailnest.example
        </li>
        <li>
          <svg viewBox="0 0 16 16" aria-hidden="true"><circle cx="8" cy="8" r="7" fill="var(--accent)"/><path d="M1 8h14M8 1c-3 3.5-3 10.5 0 14M8 1c3 3.5 3 10.5 0 14" stroke="#fff" stroke-width="1" fill="none"/></svg>
          www.corwincresthomes.example
        </li>
      </ul>
      <p class="details__license">License: CORWICH462KX</p>
    </div>
  </section>
</main>
</body>
</html>
```